Wordpress Design Project (Lanternfield)

We need a wordpress design for an established auction and real estate company based in California. The winning design will incorporate a creative layout, pleasing color scheme and logo in a very professional and clean manner.

Industry/Entity Type

Real Estate

Requirements
Must have
• Client likes the overall look of http://pelkora.com/. Site will use the logo colors and maybe complimentary highlight color. Note from client: "“It's important that the appearance of the site will be unique and easily recognizable. In general try to avoid too many colors especially bright and negative contention colors such as bright red, orange, yellow and such. "

The layout should be close as the mentioned reference site except the slideshow (image attached) should be placed below navigation, perhaps at top of content area for the page. Sidebar widgets will include:
- SMS signup form
- Register to bid call to action (as in reference site)
- Email signup form (with only "enter email" field)
- Blog feature "News & Events"
- Social media icons for facebook, twitter, google+, RSS

Navigation:
1) Home
2) Auctions
3) Online Auctions
4) Past Auctions
5) About Us
6) FAQ
7) Blog
8) Contact Us
Nice to have
• Site will have drop-down menus, idea of these would be nice for any of the primary navigation tabs.
Should not have
• please use no auction gavels in the design

```html
<!DOCTYPE html>
<html lang="en">
<head>
<meta charset="utf-8">
<title>Lanternfield Auctions</title>
<link href="https://fonts.googleapis.com/css2?family=PT+Serif:wght@400;700&family=Arimo:wght@400;700&family=Roboto:wght@500;700&display=swap" rel="stylesheet">
<style>
:root{
  --teal:#1d7466;
  --teal-dark:#0d4a40;
  --sky:#2b9eab;
  --rust:#b45c49;
  --rust-dark:#9a4737;
  --ink:#222;
  --grey-bg:#8b8b8b;
  --panel:#fff;
  --soft:#eef7f8;
}
*{box-sizing:border-box;margin:0;padding:0}
html,body{width:1108px;height:1200px;overflow:hidden}
body{font-family:"Arimo",Arial,sans-serif;color:var(--ink);
  background:linear-gradient(180deg,var(--sky) 0,#8fd0d6 90px,#f4f8f8 150px,#d8d8d8 420px,#a8a8a8 800px,var(--grey-bg) 1200px);}
.canvas{position:relative;width:1108px;height:1200px}
.abs{position:absolute}
.brand{left:96px;top:40px;display:flex;align-items:center;gap:10px;font-family:"PT Serif",serif;font-weight:700;font-size:24px;color:var(--teal-dark)}
.brand .mark{width:22px;height:22px;background:var(--teal-dark)}
.social{right:93px;top:53px;display:flex;gap:14px}
.social span{width:39px;height:39px;border-radius:7px;display:block;box-shadow:0 2px 3px rgba(0,0,0,.3)}
.social .s1{background:#3c5a98}.social .s2{background:#4fb4d8}.social .s3{background:#c9c9cc}.social .s4{background:#e8702b}
.panel{left:94px;top:142px;width:918px;height:894px;background:var(--panel);border-radius:4px}
.nav{left:100px;top:147px;width:906px;height:46px;border-radius:6px;background:linear-gradient(180deg,var(--teal),var(--teal-dark));display:flex;align-items:center;justify-content:space-between;padding:0 22px;font-family:"PT Serif",serif;font-size:14px;color:#fff;text-transform:uppercase}
.nav .sep{width:1px;height:22px;background:rgba(255,255,255,.25)}
.nav .active{position:relative}
.nav .active:after{content:"";position:absolute;left:50%;top:20px;margin-left:-4px;border:4px solid transparent;border-top-color:#fff}
.drop{left:464px;top:194px;width:146px;height:128px;background:var(--teal-dark);border-radius:0 0 6px 6px;padding:6px 5px;z-index:3;font-size:13.5px;color:#fff}
.drop li{list-style:none;height:28px;line-height:28px;padding-left:13px;margin-bottom:2px}
.drop li.on{background:var(--rust);border-radius:5px;opacity:.9}
.box{border-radius:6px}
.register{left:101px;top:204px;width:258px;height:257px;border:1px solid #e2e2e2;background:linear-gradient(180deg,#fff,var(--soft));text-align:center;padding-top:14px}
.register h2{font-family:"PT Serif",serif;font-size:27px;color:var(--teal-dark);letter-spacing:.3px}
.register p{font-size:15.5px;line-height:20px;margin:6px 12px 0}
.register .art{width:170px;height:100px;margin:10px auto 0;background:radial-gradient(ellipse at 50% 45%,#d86a50 0,#f4d0c6 45%,rgba(255,255,255,0) 72%)}
.btn-teal{display:inline-block;margin-top:12px;width:146px;height:43px;border-radius:14px;background:linear-gradient(180deg,#2a8a7b,var(--teal-dark));color:#fff;font-family:"Roboto",sans-serif;font-weight:700;font-size:17px;line-height:43px}
.alerts{left:101px;top:483px;width:258px;height:131px;background:linear-gradient(180deg,var(--teal),var(--teal-dark));padding:12px 12px}
.sms{left:101px;top:632px;width:258px;height:174px;background:linear-gradient(180deg,var(--rust),var(--rust-dark));padding:9px 12px}
.side-title{font-family:"PT Serif",serif;font-weight:700;font-size:19px;color:#fff}
.field{height:31px;border-radius:4px;background:linear-gradient(180deg,#fff,#e4e4e4);font-size:12px;line-height:31px;padding-left:8px;margin-top:10px;color:#333}
.btn-dark{display:flex;align-items:center;justify-content:center;gap:9px;margin:10px auto 0;width:139px;height:34px;border-radius:6px;background:linear-gradient(180deg,#4a4a4a,#111);color:#fff;font-family:"Roboto",sans-serif;font-weight:500;font-size:18px}
.news{left:101px;top:825px;width:258px;height:199px;border:1px solid #e8e8e8;background:linear-gradient(180deg,#fff,#e6e6e6);padding:10px 12px}
.news h3{font-family:"PT Serif",serif;font-size:19px;color:var(--teal-dark);margin-bottom:10px}
.news .item{padding-left:14px;position:relative;font-size:11px;line-height:13px;margin-bottom:8px;padding-bottom:8px;border-bottom:1px dotted #bbb}
.news .item:last-of-type{border:0}
.news .item:before{content:"»";position:absolute;left:0;top:0;font-weight:700;font-size:12px}
.news .item b{display:block;color:var(--teal-dark);font-size:11.5px;margin-bottom:4px}
.news .more{text-align:right;font-weight:700;font-size:11.5px;color:#333}
.slider{left:375px;top:206px;width:631px;height:256px;border-radius:6px;background:linear-gradient(135deg,#4a2a1a,#a36a34 35%,#d5a65a 60%,#6a3b22)}
.welcome{left:378px;top:484px;width:620px}
.welcome h1{font-family:"PT Serif",serif;font-weight:400;font-size:21px;color:var(--rust)}
.welcome p{font-size:12.5px;line-height:17px;margin-top:9px}
.upcoming{left:380px;top:576px;font-size:17px;font-weight:400;letter-spacing:.2px}
.card{left:380px;top:606px;width:604px;height:360px;border:1px solid #ddd;border-radius:4px;background:linear-gradient(180deg,#fff,#e8e8e8);overflow:hidden}
.card-head{height:35px;background:linear-gradient(180deg,var(--teal),var(--teal-dark));color:#fff;font-weight:700;font-size:14px;line-height:35px;padding-left:10px;letter-spacing:.3px}
.thumb{left:12px;top:64px;width:137px;height:96px;border:1px solid #2b5aa0;background:linear-gradient(180deg,#7fa6c6,#c8c8c0 50%,#4d7a3a)}
.details{left:11px;top:176px;width:139px;height:34px;border-radius:6px;background:linear-gradient(180deg,#c36a55,var(--rust-dark));color:#fff;font-family:"Roboto",sans-serif;font-weight:700;font-size:16px;display:flex;align-items:center;justify-content:center;gap:10px}
.lot{left:170px;top:70px;width:420px;font-size:13px;line-height:15.5px}
.lot .t{color:var(--teal-dark);font-weight:700;font-size:13.5px;line-height:17px;margin-bottom:6px}
.timing{left:172px;top:192px;font-size:13px;line-height:20px}
.timing .only{color:var(--teal-dark);font-weight:700;font-size:12px;margin-bottom:4px}
.bid{left:172px;top:268px;width:305px;height:42px;border-radius:6px;background:linear-gradient(180deg,#4a4a4a,#0e0e0e);color:#fff;font-family:"Roboto",sans-serif;font-weight:700;font-size:14px;display:flex;align-items:center;justify-content:center;gap:12px;letter-spacing:.4px}
.footer{left:93px;top:1063px;width:920px;height:103px;border-radius:6px;background:linear-gradient(180deg,var(--teal),var(--teal-dark));color:#fff}
.footer .brand-f{left:18px;top:38px;display:flex;align-items:center;gap:8px;font-family:"PT Serif",serif;font-weight:700;font-size:17px;color:#fff}
.footer .brand-f i{width:16px;height:16px;background:#fff;display:block}
.footer .links{left:272px;top:24px;font-size:12px;word-spacing:2px}
.footer .info{left:250px;top:47px;width:450px;text-align:center;font-size:12px;line-height:21px}
</style>
</head>
<body>
<div class="canvas">
  <header>
    <div class="abs brand"><span class="mark"></span>Lanternfield Auctions</div>
    <div class="abs social" aria-label="Social links"><span class="s1"></span><span class="s2"></span><span class="s3"></span><span class="s4"></span></div>
  </header>

  <div class="abs panel"></div>

  <nav class="abs nav">
    <span>Home</span><i class="sep"></i><span>Auctions</span><i class="sep"></i><span>Online Auctions</span><i class="sep"></i><span class="active">Past Auctions</span><i class="sep"></i><span>About Us</span><i class="sep"></i><span>FAQ</span><i class="sep"></i><span>Blog</span><i class="sep"></i><span>Contact Us</span>
  </nav>
  <ul class="abs drop">
    <li>Past Auction #</li><li class="on">Past Auction #</li><li>Past Auction #</li><li>Past Auction #</li>
  </ul>

  <aside>
    <section class="abs box register">
      <h2>REGISTER TO BID</h2>
      <p>Find great deals at our online auctions</p>
      <div class="art" role="img" aria-label="Bid illustration with computer mouse"></div>
      <span class="btn-teal">Register Now</span>
    </section>
    <section class="abs box alerts">
      <div class="side-title">Sign up for Auction Alerts</div>
      <div class="field">Enter your email</div>
      <div class="btn-dark"><svg width="24" height="18" viewBox="0 0 24 18"><rect x="1" y="1" width="22" height="16" rx="2" fill="#fff"/><path d="M1 2l11 8 11-8" stroke="#333" stroke-width="1.6" fill="none"/></svg>Join Now</div>
    </section>
    <section class="abs box sms">
      <div class="side-title">SMS Sign Up</div>
      <div class="field">Enter your email</div>
      <div class="field" style="margin-top:15px">Enter your phone number</div>
      <div class="btn-dark" style="margin-top:13px"><svg width="16" height="24" viewBox="0 0 16 24"><rect x="2" y="1" width="12" height="22" rx="2" fill="none" stroke="#fff" stroke-width="2"/><circle cx="8" cy="19" r="1.5" fill="#fff"/></svg>Sign Up</div>
    </section>
    <section class="abs box news">
      <h3>News &amp; Events</h3>
      <div class="item"><b>Lorem Ipsum is simply dummytext</b>Lorem Ipsum is simply dummy text of the printing and typesetting industry.</div>
      <div class="item"><b>Lorem Ipsum is simply dummytext</b>Lorem Ipsum is simply dummy text of the printing and typesetting industry.</div>
      <div class="more">More News [+]</div>
    </section>
  </aside>

  <main>
    <div class="abs slider" role="img" aria-label="Slideshow photo of an antiques showroom with cabinets, china and sunflowers"></div>
    <section class="abs welcome">
      <h1>WELCOME TO LANTERNFIELD AUCTIONS</h1>
      <p>If you are going to use a passage of Lorem Ipsum, you need to be sure there isn't anything embarrassing hidden in the middle of text.</p>
    </section>
    <h2 class="abs upcoming">UPCOMING&nbsp; LIVE &amp; ONLINE AUCTIONS</h2>
    <article class="abs card">
      <div class="card-head">MARLOWE PHYSICAL THERAPY IN ASHFORD HOLLOW, GA</div>
      <div class="abs thumb" role="img" aria-label="Photo of a large white house with lawn"></div>
      <div class="abs details"><svg width="22" height="22" viewBox="0 0 22 22"><circle cx="9" cy="9" r="6.5" fill="none" stroke="#fff" stroke-width="2"/><path d="M14 14l6 6" stroke="#fff" stroke-width="2.5"/></svg>DETAILS</div>
      <div class="abs lot">
        <div class="t">Tanner Vale Auctions, LLC GAL 5108 - Everything sold to the high bidder</div>
        Location:<br>Location 1 - 412 Orchard Ridge Hwy<br>Location 2 - 58 Willow Bend # 3<br>Ashford Hollow, GA 30999
      </div>
      <div class="abs timing">
        <div class="only">Online Bidding Only</div>
        Began:&nbsp; Friday, May 24, 2013 at 10:06 AM EDT<br>Ends:&nbsp; Wednesday, June 05, 2013 at 10:00 AM EDT
      </div>
      <div class="abs bid"><svg width="22" height="20" viewBox="0 0 22 20"><rect x="1" y="1" width="20" height="13" fill="none" stroke="#fff" stroke-width="2"/><path d="M7 18h8M11 14v4" stroke="#fff" stroke-width="2"/></svg>CLICK HERE FOR ONLINE BIDDING</div>
    </article>
  </main>

  <footer class="abs footer">
    <div class="abs brand-f"><i></i>Lanternfield Auctions</div>
    <div class="abs links">Home&nbsp; | &nbsp;Auctions&nbsp; | &nbsp;Online Auctions&nbsp; | &nbsp;Past Auctions&nbsp; | &nbsp;About Us&nbsp; | &nbsp;FAQ&nbsp; | &nbsp;Blog&nbsp; | &nbsp;Contact Us</div>
    <div class="abs info">Phone: 555- 014-2290, Email: info@lanternfieldbids.com<br>Copyright&nbsp; Lanternfield Auction 2013 - 2014 .&nbsp; All Rights Reserved</div>
  </footer>
</div>
</body>
</html>
```